Business Card Design Project for Food Export Company

Introduction about my Company Meng Tai Export Pte. Ltd.
(Meng Tai Food Export)
A Sole Distributor of various products:
Brand
Soy Powder (Brand: Bean Bean)
Coffee Powders (Brand: Ruvo)
OEM products
- Cocoa Powder
- Green Tea Powder
- Almond Powder
- Almond Flavour Powder
Showing we are professional with decades of experiences in terms of Product Quality and Trust.
NAMECARD - 2 sided namecard
Front:
Informations:
Darren Low
Sales Executive
+65 90428317
darrenlow@mtfoodtrade.example
Meng Tai Export Pte. Ltd.
42 Tuas Crescent, #03-08 Meridian Tower
Singapore 638102
Back:
Sole Distributor:
Bean Bean and Ruvoe
OEM Products:
Cocoa Powder / Green Tea Powder / Almond Powder / Almond Flavour Powder / Ice Cream Powder
I have attached Meng Tai Export's Logos. I've 2 currently, I would like to see some comparison.
Attached 2 Logos for Ruvo and Bean Bean.
Updates
Hi all designers,
I've revised the brief.
Have a look.
Thank you
Darren
Industry/Entity Type
Business
Look and feel

```html
<!DOCTYPE html>
<html lang="en">
<head>
<meta charset="utf-8">
<title>Meng Tai Food Export – Business Card</title>
<link rel="stylesheet" href="https://fonts.googleapis.com/css2?family=Cinzel:wght@400;600&family=Montserrat:ital,wght@0,400;0,600;1,400&display=swap">
<style>
  :root {
    --stage-light: #ffffff;
    --stage-edge: #e4e4e4;
    --band: #231f20;
    --card-light: #e8dfc6;
    --card-mid: #dbcfae;
    --card-dark: #cfc099;
    --brand-red: #9e1b1f;
    --ink: #2a2622;
    --ink-soft: #4a453f;
    --white: #ffffff;
  }
  * { margin: 0; padding: 0; box-sizing: border-box; }
  html, body { width: 1200px; height: 900px; overflow: hidden; }
  body {
    position: relative;
    background: radial-gradient(ellipse 70% 55% at 50% 40%, var(--stage-light) 40%, var(--stage-edge) 100%);
    font-family: "Montserrat", Arial, sans-serif;
    color: var(--ink);
  }
  .card {
    position: absolute;
    top: 229px;
    width: 419px;
    height: 238px;
    background:
      radial-gradient(ellipse 60% 50% at 70% 30%, rgba(255,255,255,.35), transparent 70%),
      radial-gradient(ellipse 50% 60% at 20% 80%, rgba(160,140,90,.18), transparent 70%),
      linear-gradient(135deg, var(--card-mid), var(--card-light) 55%, var(--card-dark));
    box-shadow: 0 2px 6px rgba(0,0,0,.18);
    text-align: center;
  }
  .card--back { left: 150px; }
  .card--front { left: 631px; }

  .brand-name {
    position: absolute;
    left: 0; right: 0;
    top: 98px;
    font-family: "Cinzel", Georgia, serif;
    font-weight: 400;
    font-size: 15px;
    letter-spacing: .5px;
    color: var(--brand-red);
  }

  .product-list {
    position: absolute;
    top: 159px;
    left: 0; right: 0;
    font-family: "Cinzel", Georgia, serif;
    font-size: 10px;
    line-height: 12px;
    color: var(--ink);
  }
  .product-list p + p { margin-top: 4px; }

  .contact {
    position: absolute;
    top: 47px;
    left: 0; right: 0;
    text-align: center;
  }
  .contact__name {
    font-family: "Cinzel", Georgia, serif;
    font-weight: 400;
    font-size: 21px;
    color: var(--brand-red);
    letter-spacing: .5px;
  }
  .contact__role {
    font-weight: 600;
    font-size: 10.5px;
    letter-spacing: .5px;
    margin-top: 2px;
  }
  .contact__lines { margin-top: 6px; font-size: 13px; line-height: 17.5px; }
  .contact__address {
    margin-top: 9px;
    font-style: italic;
    font-size: 10.5px;
    line-height: 13px;
    color: var(--ink-soft);
  }

  .footer-band {
    position: absolute;
    left: 0; right: 0; bottom: 0;
    height: 205px;
    background: var(--band);
  }
  .footer-brand {
    position: absolute;
    right: 152px;
    top: 784px;
    font-family: "Cinzel", Georgia, serif;
    font-weight: 400;
    font-size: 22px;
    letter-spacing: .5px;
    color: var(--white);
  }
</style>
</head>
<body>
  <section class="card card--back">
    <p class="brand-name">MENG TAI FOOD EXPORT</p>
    <div class="product-list">
      <p>SOLE DISTRIBUTOR:&nbsp; BEAN BEAN AND RUVOE</p>
      <p>OEM PRODUCTS:&nbsp; COCOA POWDER · GREEN TEA POWDER<br>
      ALMOND POWDER · ALMOND FLAVOUR POWDER<br>
      ICE CREAM POWDER</p>
    </div>
  </section>

  <section class="card card--front">
    <div class="contact">
      <h1 class="contact__name">DARREN LOW</h1>
      <p class="contact__role">SALES EXECUTIVE</p>
      <p class="contact__lines">(+65) 90428317<br>darrenlow@mtfoodtrade.example<br>www.mengtaiexport.example</p>
      <p class="contact__address">Address: 42 Tuas Crescent,<br>#03-08 Meridian Tower<br>Singapore 638102</p>
    </div>
  </section>

  <footer class="footer-band"></footer>
  <p class="footer-brand">MENG TAI FOOD EXPORT</p>
</body>
</html>
```